Marvela Oil & Gas Exploation and Production Company Website

Need a website for an independent Oil and Gas Company. Want the design to be Conservative, Professional and Traditional Feeling. Use colors from Logo or soft tones. See Doc for thoughts on layout.

Not sure why this is showing desgins due. Try to work with QP to extend a couple days.

Target Market(s)

Mineral Owners, Investors, Potential Employees, Services Partners

Industry/Entity Type

Oil & Gas Exlploration and Production

Coding

Coded - Design and coding required

Number of Pages Required

5+ page

Colors
0054AA
0677BA
7BADD7
CADEEF
E8F1F8

Requirements
Must have
• Use best picture of rigs or landscape as you see fit, do nto have to use all picuters
Nice to have
• You can look at traditional Website for Portfolio companies exmaples at https://www.halvorcapital.example/about/upstream/portfolio, or https://brisonpower.example/our-portfolio/

```html
<!DOCTYPE html>
<html lang="en">
<head>
<meta charset="utf-8">
<title>Marvela Oil &amp; Gas</title>
<link rel="stylesheet" href="https://fonts.googleapis.com/css2?family=Oswald:wght@500;600&family=Outfit:wght@300;400;500;700&display=swap">
<style>
:root{
  --blue:#0f56a8;
  --blue-dark:#0c4f9e;
  --ink:#111111;
  --grey:#666a70;
  --band-light:#f1f4f9;
  --band-mid:#e5e9f2;
  --panel:#f2f5fa;
  --line:#d9dde4;
  --white:#ffffff;
}
*{box-sizing:border-box;margin:0;padding:0}
html,body{width:1200px;height:3320px;overflow:hidden}
body{font-family:'Outfit',sans-serif;color:var(--ink);background:var(--white);position:relative}
.heading{font-family:'Oswald',sans-serif;font-weight:500;font-size:48px;line-height:1;letter-spacing:-0.5px;text-transform:uppercase;color:var(--ink)}
.heading .accent{color:var(--blue)}
.wordmark{font-family:'Outfit',sans-serif;font-weight:700;color:var(--blue);letter-spacing:1px;line-height:1}

/* hero */
.hero{position:absolute;left:0;top:0;width:1200px;height:688px;
  background:linear-gradient(180deg,#f4efe6 0%,#f3dba0 30%,#efc45a 55%,#c9a24a 72%,#4f6a2a 84%,#5f8a2c 100%)}
.hero .wordmark{position:absolute;left:116px;top:42px;font-size:40px}
.nav{position:absolute;right:122px;top:54px;display:flex;gap:31px;font-family:'Oswald',sans-serif;font-weight:500;font-size:15px;text-transform:uppercase;color:var(--ink)}
.hero-text{position:absolute;left:330px;top:260px;width:680px;font-size:30px;line-height:36px;font-weight:400;color:#1a1a1a}

/* about */
.about{position:absolute;left:0;top:688px;width:1200px;height:479px}
.about .heading{position:absolute;left:116px;top:82px}
.about-lead{position:absolute;left:116px;top:152px;width:580px;font-size:18.5px;font-weight:700;line-height:29px}
.about-body{position:absolute;left:116px;top:250px;width:580px;font-size:18px;font-weight:300;line-height:26px;color:var(--grey)}
.about-photo{position:absolute;left:740px;top:62px;width:340px;height:354px;border-radius:50%;
  background:linear-gradient(180deg,#2a62a8 0%,#8fb2d6 40%,#e7c59a 70%,#d98b4a 100%)}

/* operations */
.operations{position:absolute;left:0;top:1167px;width:1200px;height:525px;background:var(--band-light)}
.operations .heading{position:absolute;left:116px;top:60px}
.operations .sub{position:absolute;left:116px;top:118px;font-size:17px;font-weight:700}
.legend{position:absolute;left:117px;top:291px;width:243px;height:188px;background:var(--white);border:1px solid var(--line);padding:10px 17px}
.legend h3{font-size:20px;font-weight:700;margin-bottom:8px}
.legend li{list-style:none;display:flex;align-items:center;gap:12px;font-size:20px;height:35px}
.legend i{display:block;width:37px;height:18px}
.map{position:absolute;left:625px;top:25px;width:445px;height:478px;background:linear-gradient(135deg,#ffffff 0%,#f3f3f3 55%,#d9ecc8 75%,#f7c2a6 100%);border:1px solid #cfd3d9}

/* related */
.related{position:absolute;left:0;top:1692px;width:1200px;height:307px;background:var(--band-mid)}
.related .heading{position:absolute;left:0;width:1200px;text-align:center;top:56px}
.entities{position:absolute;left:109px;top:149px;display:flex;gap:16px}
.entity{width:232px;height:98px;background:var(--white);border:3px solid #f5f6f9;outline:1px solid var(--line);padding:12px 12px 0}
.entity .wordmark{font-size:40px;display:block}
.entity span{display:block;text-align:right;font-size:19px;color:#333;margin-top:8px}
.entity.first span{text-align:left}

/* team */
.team{position:absolute;left:0;top:1999px;width:1200px;height:566px}
.team .heading{position:absolute;left:0;width:1200px;text-align:center;top:66px}
.members{position:absolute;left:113px;top:164px;display:flex;gap:28px}
.member{width:304px;height:375px;border:1px solid var(--line);padding:7px;text-align:center}
.member .photo{width:288px;height:289px;background:radial-gradient(circle at 50% 45%,#8e9db1 0%,#3a4a63 60%,#1e2430 100%)}
.member h3{font-family:'Oswald',sans-serif;font-weight:500;font-size:30px;color:var(--blue);margin-top:6px;line-height:40px}
.member p{font-size:20px;color:#333;line-height:24px}

/* contact */
.contact{position:absolute;left:0;top:2565px;width:1200px;height:755px}
.contact .heading{position:absolute;left:0;width:1200px;text-align:center;top:57px}
.directions{position:absolute;left:113px;top:150px;width:520px;height:546px;background:var(--panel);padding:40px 45px}
.panel-title{font-family:'Oswald',sans-serif;font-weight:500;font-size:34px;text-transform:uppercase;color:var(--blue);line-height:1}
.directions h4{font-size:24px;font-weight:400;margin-top:40px;line-height:30px}
.directions h4+p{margin-top:10px}
.directions p{font-size:19px;font-weight:300;line-height:30px;color:#333}
.directions .copyright{position:absolute;left:45px;bottom:28px;font-size:16px;font-weight:400;color:#222}
.touch{position:absolute;left:655px;top:150px;width:425px;height:546px;background:var(--blue-dark);padding:28px 29px}
.touch .panel-title{color:var(--white);text-align:center;margin-bottom:33px}
.field{display:block;width:367px;height:57px;background:var(--white);margin-bottom:21px;padding:0 13px;font-size:18px;font-weight:300;color:#9a9ea5;line-height:57px}
.field.area{height:128px;line-height:1;padding-top:18px}
.submit{position:absolute;right:29px;bottom:25px;width:151px;height:57px;border:2px solid #5f8fcf;color:var(--white);font-size:21px;font-weight:300;text-align:center;line-height:53px}
</style>
</head>
<body>

<header class="hero" role="img" aria-label="Drilling rig standing in a green field at sunset">
  <div class="wordmark">MARVELA</div>
  <nav class="nav"><span>Home</span><span>About</span><span>Operations</span><span>Management</span><span>Contact</span></nav>
  <p class="hero-text">Experienced upstream oil and gas company focused a lease and drill development strategy that quickly brings cash returns to its investors and royalty owners.</p>
</header>

<section class="about">
  <h2 class="heading">About <span class="accent">Marvela</span></h2>
  <p class="about-lead">Marvela Oil &amp; Gas, LLC was formed to pursue upstream acquisition and development opportunities in January 2022 by Grant Whitlow and Martin Okafor.</p>
  <p class="about-body">Marvela is focused on “Lease and Drill” opportunities in Unconventional Reservoirs.&nbsp; Marvela is also evaluating opportunities with existing production (&lt;50% of purchase price) and with high-quality development upside.&nbsp; Marvela is currently funded by knowledgeable accredited inventors of the upstream sector, including family offices, Individuals and Traditional GP/Asset Managers.</p>
  <div class="about-photo" role="img" aria-label="Pump jacks and a rig silhouetted against a sunset sky, in a round frame"></div>
</section>

<section class="operations">
  <h2 class="heading">Operations</h2>
  <p class="sub">Currently leasing in Ohio.</p>
  <div class="legend">
    <h3>Legend</h3>
    <ul>
      <li><i style="background:#f47f7f"></i>BRAMBLE</li>
      <li><i style="background:#b5dfa0"></i>Oil Window</li>
      <li><i style="background:#fbf2dc"></i>Wet Gas Window</li>
      <li><i style="background:#f8bd9b"></i>Dry Gas Window</li>
    </ul>
  </div>
  <div class="map" role="img" aria-label="County map of Ohio with the oil, wet gas and dry gas windows shaded along the eastern edge"></div>
</section>

<section class="related">
  <h2 class="heading">Related Entities</h2>
  <div class="entities">
    <div class="entity first"><span class="wordmark">MARVELA</span><span>Oil and Gas OHIO LLC</span></div>
    <div class="entity"><span class="wordmark">MARVELA</span><span>Oil and Gas LLC</span></div>
    <div class="entity"><span class="wordmark">MARVELA</span><span>Oil and Gas II LLC</span></div>
    <div class="entity"><span class="wordmark">MARVELA</span><span>Minerals LLC</span></div>
  </div>
</section>

<section class="team">
  <h2 class="heading">Management <span class="accent">Team</span></h2>
  <div class="members">
    <div class="member"><div class="photo" role="img" aria-label="Portrait of Grant Whitlow"></div><h3>Grant Whitlow</h3><p>President &amp; CEO</p></div>
    <div class="member"><div class="photo" role="img" aria-label="Portrait of Martin Okafor"></div><h3>Martin Okafor</h3><p>CFO &amp; Advisor</p></div>
    <div class="member"><div class="photo" role="img" aria-label="Portrait of Dale Ramsey"></div><h3>Dale Ramsey</h3><p>Vice President - Land</p></div>
  </div>
</section>

<section class="contact">
  <h2 class="heading">Contact <span class="accent">Us</span></h2>
  <div class="directions">
    <h3 class="panel-title">Directions</h3>
    <h4>Mailing Address</h4>
    <p>2281 Lindenwood Dr #4410<br>Houston, Texas 77054</p>
    <h4>Office Address</h4>
    <p>815 Carrow St. Suite 2100<br>Houston, Texas 77003</p>
    <p class="copyright">Copyright 2023 Marvela Oil &amp; Gas LLC</p>
  </div>
  <div class="touch">
    <h3 class="panel-title">Get in Touch</h3>
    <span class="field">Your Name</span>
    <span class="field">Email Address</span>
    <span class="field">Phone</span>
    <span class="field area">Description of interest</span>
    <span class="submit">Submit</span>
  </div>
</section>

</body>
</html>
```